Business Card Design Project

I am seeking a business card for my life coaching career. I specialize in coaching executives and entrepreneurs. Consciousness plays a key role in my practice.
Updates

I would like to see different fonts -I don't like the way the capital J looks. I only want my name once on the card, on the front. I like everything centered on the front, with a white background, grey and green on the front; and the same grey on the back with bullet points next to each quality; centered. I like a subtle shadow of the mountains behind the text on the back of the card. I don't want the mountains on either side to be too big. Thank you.

Target Market(s)

Middle age business owners/executives

Industry/Entity Type

Business

Contact Information for Business Card

The front design is my name and a mountain logo. I want to have my name prominently shown.

Requirements
Must have
• Front of card:
• My name prominent sized font
• Helping clients lead more fulfilling lives;
• Executive Life Coach
• 555-304-7781
• rkovet4@mailbriar.com
• Back of Card:
• Providing Unparalleled support
• Providing a safe place to grow in self-awareness
• 20+ years entrepreneurial experience
• Trust
• Integrity
Nice to have
• Easy to read font; warm colors reflecting a masculine personality.

Files

```html
<!DOCTYPE html>
<html lang="en">
<head>
<meta charset="utf-8">
<title>Rowan Hale – Business Card</title>
<link href="https://fonts.googleapis.com/css2?family=Montserrat:wght@600;700&family=Open+Sans:wght@400;600&display=swap" rel="stylesheet">
<style>
  :root {
    --bg: #d9dbd9;
    --card: #ffffff;
    --green: #5b7a3c;
    --green-light: #8cc63f;
    --grey: #4a4a4a;
    --white: #ffffff;
  }
  * { margin: 0; padding: 0; box-sizing: border-box; }
  html, body { width: 1200px; height: 772px; overflow: hidden; }
  body {
    background: var(--bg);
    font-family: "Open Sans", Arial, sans-serif;
    display: flex;
    align-items: center;
    justify-content: center;
    gap: 40px;
  }
  .card {
    position: relative;
    width: 540px;
    height: 310px;
    background: var(--card);
    box-shadow: 0 6px 18px rgba(0,0,0,0.18);
    overflow: hidden;
  }

  /* Brand side */
  .card--front {
    display: flex;
    flex-direction: column;
    align-items: center;
    justify-content: center;
    gap: 8px;
  }
  .brand {
    display: flex;
    align-items: center;
    gap: 14px;
  }
  .brand__mark {
    width: 20px;
    height: 20px;
    background: var(--green);
  }
  .brand__name {
    font-family: "Montserrat", Arial, sans-serif;
    font-weight: 700;
    font-size: 50px;
    line-height: 1.1;
    color: var(--green);
    letter-spacing: 1px;
  }
  .tagline {
    font-family: "Montserrat", Arial, sans-serif;
    font-weight: 600;
    font-size: 14px;
    color: var(--grey);
    letter-spacing: 0.5px;
  }
  .qualities {
    list-style: none;
    margin-top: 10px;
    text-align: center;
    font-size: 11.5px;
    line-height: 1.7;
    color: var(--grey);
  }
  .qualities li::before {
    content: "";
    display: inline-block;
    width: 6px;
    height: 6px;
    border-radius: 50%;
    background: var(--green);
    margin-right: 8px;
    vertical-align: middle;
  }

  /* Contact side */
  .card__waves { position: absolute; inset: 0; }
  .info-brand {
    position: absolute;
    top: 26px;
    right: 30px;
    text-align: right;
  }
  .info-brand__name {
    display: flex;
    align-items: center;
    justify-content: flex-end;
    gap: 8px;
    font-family: "Montserrat", Arial, sans-serif;
    font-weight: 700;
    font-size: 28px;
    color: var(--green);
  }
  .info-brand__mark { width: 12px; height: 12px; background: var(--green); }
  .info-brand__tagline {
    font-size: 9px;
    color: var(--grey);
    margin-top: 2px;
  }
  .person {
    position: absolute;
    left: 30px;
    top: 150px;
  }
  .person__name {
    font-family: "Montserrat", Arial, sans-serif;
    font-weight: 600;
    font-size: 17px;
    letter-spacing: 1px;
    color: var(--green-light);
  }
  .person__role {
    font-size: 11px;
    letter-spacing: 1.5px;
    color: var(--white);
    margin-top: 2px;
  }
  .address {
    position: absolute;
    left: 30px;
    bottom: 24px;
    font-size: 11px;
    line-height: 1.5;
    color: var(--white);
  }
  .contacts {
    position: absolute;
    right: 30px;
    bottom: 20px;
    list-style: none;
    font-size: 10.5px;
    line-height: 1.75;
    color: var(--white);
  }
  .contacts li { display: flex; align-items: center; gap: 7px; }
  .contacts svg { width: 10px; height: 10px; fill: var(--green-light); }
</style>
</head>
<body>

  <section class="card card--front">
    <div class="brand">
      <span class="brand__mark"></span>
      <span class="brand__name">Rowan Hale</span>
    </div>
    <p class="tagline">Helping clients lead more fulfilling lives</p>
    <ul class="qualities">
      <li>Providing unparalleled support</li>
      <li>Providing a safe place to grow in self-awareness</li>
      <li>20+ years entrepreneurial experience</li>
      <li>Trust</li>
      <li>Integrity</li>
    </ul>
  </section>

  <section class="card card--info">
    <svg class="card__waves" viewBox="0 0 540 310" preserveAspectRatio="none" aria-hidden="true">
      <path d="M0 128 C150 108 330 150 540 112 L540 136 C330 172 150 134 0 150 Z" fill="var(--grey)"/>
      <path d="M0 142 C150 124 330 166 540 128 L540 310 L0 310 Z" fill="var(--green)"/>
    </svg>

    <div class="info-brand">
      <div class="info-brand__name"><span class="info-brand__mark"></span>Rowan Hale</div>
      <p class="info-brand__tagline">Helping clients lead more fulfilling lives</p>
    </div>

    <div class="person">
      <p class="person__name">DANIEL MERCER</p>
      <p class="person__role">EXECUTIVE LIFE COACH</p>
    </div>

    <p class="address">214 Cedar Ridge Lane<br>Aspen Hollow</p>

    <ul class="contacts">
      <li><svg viewBox="0 0 10 10"><path d="M2 0h2l1 2.5-1.3 1a6 6 0 0 0 2.8 2.8l1-1.3L10 6v2a2 2 0 0 1-2 2A8 8 0 0 1 0 2a2 2 0 0 1 2-2z"/></svg>555-304-7781</li>
      <li><svg viewBox="0 0 10 10"><rect x="1" y="3" width="8" height="6" rx="1"/><rect x="3" y="0" width="4" height="3"/></svg>555-304-7781</li>
      <li><svg viewBox="0 0 10 10"><rect x="2.5" y="0" width="5" height="10" rx="1"/></svg>555-304-7781</li>
      <li><svg viewBox="0 0 10 10"><path d="M0 2h10v6H0z M0 2l5 3.5L10 2"/></svg>rkovet4@mailbriar.com</li>
      <li><svg viewBox="0 0 10 10"><circle cx="5" cy="5" r="5"/></svg>www.rowanhalecoaching.com</li>
    </ul>
  </section>

</body>
</html>
```